Project Management - Web Design Project

Vantrel 4 Management Limited is a company which provides specialist Project Control and Contract Management expertise to the Engineering, Construction and Manufacturing industries. The emphasis is on advanced Project Management techniques in particular Planning & Scheduling, Cost Control, Change Control, Risk Management, Reporting and Contract Administration. We are a global company (albeit a small start-up at this time) and pride ourselves on our ability to support projects to help them achieve their goals and objectives. Our aim is to implement work class control tools in a simple and user friendly manner. We would like the website to appear professional but at the same time easy to navigate and a good balance between text and pictures. The final design should communicate our value added service to our customers, our willingness to support and our structured approach to our work.

Target Market(s)

Project Management professionals working for engineering, construction and manufacturing organisations involved with delivering projects.

Industry/Entity Type

Construction

Requirements
Must have
• The website must include all of the content from the attached Excel brief. The company logo (attached) must also be included in the design. The design must portray a professional look and feel. Please include pictures and photographs related to project management in the engineering, construction and manufacturing industries. We may supplement with pictures of our own during the next steps.
Nice to have
• Emphasis that Vantrel 4 is available to support, guide, direct to achieve positive outcomes for the projects. We work hard at developing our customer relationships. Our employees are experienced in advanced project management techniques.
Should not have
• The design should not use old style fonts. It should look modern and professional. Do not include cartoons or silly illustrations.

```html
<!DOCTYPE html>
<html lang="en">
<head>
<meta charset="utf-8">
<title>Vantrel 4 Management Limited</title>
<link rel="stylesheet" href="https://fonts.googleapis.com/css2?family=Open+Sans:wght@400;600;700&family=Titillium+Web:wght@400;600&display=swap">
<style>
  :root {
    --ink: #333333;
    --muted: #555555;
    --brand-blue: #0b4fb8;
    --title-blue: #1155b3;
    --nav-dark: #262626;
    --nav-divider: #454545;
    --nav-active-top: #2a6de0;
    --nav-active-bottom: #0a2f9a;
    --icon-grey: #606060;
    --footer-bg: #f3f3f3;
    --line-grey: #cfcfcf;
    --top-rule: #2b2b2b;
  }
  * { box-sizing: border-box; margin: 0; padding: 0; }
  html, body { width: 1200px; height: 1200px; overflow: hidden; background: #ffffff; }
  body { position: relative; font-family: "Open Sans", Arial, sans-serif; color: var(--ink); }

  .top-rule { position: absolute; left: 0; top: 0; width: 1200px; height: 5px; background: var(--top-rule); }

  .brand { position: absolute; left: 32px; top: 30px; width: 230px; height: 135px; }
  .brand-mark { position: absolute; left: 62px; top: 0; width: 80px; height: 80px; border-radius: 50%; background: var(--brand-blue); }
  .brand-name { position: absolute; left: 0; top: 92px; font-family: "Titillium Web", Arial, sans-serif; font-weight: 400; font-size: 31px; line-height: 1; letter-spacing: 1px; color: var(--icon-grey); white-space: nowrap; }
  .brand-sub { position: absolute; left: 2px; top: 124px; font-family: "Titillium Web", Arial, sans-serif; font-weight: 400; font-size: 12.5px; letter-spacing: 2.3px; color: var(--icon-grey); white-space: nowrap; }

  .social { position: absolute; top: 68px; left: 1000px; display: flex; gap: 14px; list-style: none; }
  .social li { width: 34px; height: 34px; border-radius: 50%; background: var(--icon-grey); }

  .search { position: absolute; left: 858px; top: 126px; width: 276px; height: 40px; border: 1px solid #d3d3d3; border-radius: 3px; display: flex; background: #fff; }
  .search-field { flex: 1; padding-left: 14px; font-family: "Titillium Web", Arial, sans-serif; font-size: 15px; line-height: 38px; color: #777; }
  .search-button { width: 40px; border-left: 1px solid #d3d3d3; display: flex; align-items: center; justify-content: center; }

  .main-nav { position: absolute; left: 21px; top: 196px; width: 1151px; height: 59px; background: var(--nav-dark); border-radius: 3px; display: flex; }
  .main-nav a { display: block; height: 59px; line-height: 59px; text-align: center; font-family: "Titillium Web", Arial, sans-serif; font-size: 18px; color: #ffffff; text-decoration: none; border-right: 1px solid var(--nav-divider); }
  .main-nav a.is-active { background: linear-gradient(to bottom, var(--nav-active-top), var(--nav-active-bottom)); border-radius: 3px 0 0 3px; border-right: none; }
  .main-nav a:last-child { border-right: none; }

  .hero { position: absolute; left: 20px; top: 267px; width: 1152px; height: 458px; border: 1px solid #d8d8d8; border-radius: 3px; overflow: hidden;
    background: linear-gradient(100deg, #dfe3e8 0%, #f4f5f7 35%, #b9b2aa 55%, #eeeeee 75%, #f7f7f7 100%); }
  .hero-strip { position: absolute; left: 0; bottom: 0; width: 100%; height: 80px; background: rgba(235,236,238,0.75); }
  .hero-thumbs { position: absolute; left: 23px; top: 391px; display: flex; gap: 13px; list-style: none; }
  .hero-thumbs li { width: 58px; height: 52px; border: 2px solid #ffffff; box-shadow: 0 1px 3px rgba(0,0,0,0.3); }
  .thumb-clock { background: linear-gradient(#2a56b8, #7fa3de); }
  .thumb-team { background: linear-gradient(#c9c3bd, #6e6660); }
  .thumb-meeting { background: linear-gradient(#d8dbe0, #5c6270); }
  .thumb-pair { background: linear-gradient(#e2e2e2, #2f2f33); }

  .features { position: absolute; left: 21px; top: 763px; width: 1160px; height: 300px; }
  .feature { position: absolute; top: 0; width: 182px; }
  .feature-image { width: 182px; height: 138px; border-radius: 14px 14px 0 0; }
  .feature-title { margin-top: 15px; padding-left: 6px; font-family: Arial, sans-serif; font-weight: 700; font-size: 14px; line-height: 21px; color: var(--title-blue); height: 42px; white-space: nowrap; letter-spacing: -0.1px; }
  .feature-title.single { margin-top: 12px; height: 21px; }
  .feature-text { margin-top: 9px; padding-left: 6px; font-size: 12.8px; line-height: 20px; color: var(--ink); white-space: nowrap; }
  .feature-rule { position: absolute; left: 0; top: 266px; width: 182px; border-top: 1px dotted #777; }
  .feature-more { position: absolute; right: 6px; top: 272px; font-family: "Titillium Web", Arial, sans-serif; font-size: 16px; color: var(--ink); text-decoration: none; white-space: nowrap; }
  .feature-more::after { content: ""; display: inline-block; margin-left: 5px; border-left: 4px solid var(--ink); border-top: 4px solid transparent; border-bottom: 4px solid transparent; vertical-align: 1px; }

  .img-people { background: linear-gradient(#e7ecf2, #2e2e34); }
  .img-desk { background: linear-gradient(#bdb4ab, #2a2a2e); }
  .img-tools { background: linear-gradient(#e6f0fb, #4b8fe0); }
  .img-presenter { background: linear-gradient(#e5e7ea, #3b4a6a); }
  .img-chart { background: linear-gradient(#dbe7f5, #6d8cb6); }
  .img-projects { background: linear-gradient(#1e6fdc, #0a3f9f); }

  .site-footer { position: absolute; left: 0; top: 1103px; width: 1200px; height: 97px; background: var(--footer-bg); }
  .footer-links { position: absolute; left: 35px; top: 23px; font-size: 13px; color: var(--ink); white-space: nowrap; }
  .footer-links span.sep { margin: 0 8px; }
</style>
</head>
<body>
  <div class="top-rule"></div>

  <header>
    <div class="brand">
      <div class="brand-mark"></div>
      <div class="brand-name">VANTREL 4</div>
      <div class="brand-sub">MANAGEMENT LIMITED</div>
    </div>

    <ul class="social" aria-label="Social links">
      <li aria-label="Feed"></li>
      <li aria-label="Social network"></li>
      <li aria-label="Professional network"></li>
      <li aria-label="Microblog"></li>
    </ul>

    <form class="search" role="search">
      <div class="search-field">ENTER KEYWORD</div>
      <div class="search-button">
        <svg width="22" height="22" viewBox="0 0 22 22" aria-hidden="true">
          <circle cx="9" cy="9" r="6.5" fill="none" stroke="#2a7be0" stroke-width="3"/>
          <line x1="13.5" y1="13.5" x2="19" y2="19" stroke="#2a7be0" stroke-width="3.5" stroke-linecap="round"/>
        </svg>
      </div>
    </form>

    <nav class="main-nav">
      <a href="#" class="is-active" style="width:138px">HOME</a>
      <a href="#" style="width:146px">ABOUT US</a>
      <a href="#" style="width:139px">SERVICES</a>
      <a href="#" style="width:140px">CONTACT</a>
    </nav>
  </header>

  <section class="hero" role="img" aria-label="Photo of a professional working on a laptop in a bright office">
    <div class="hero-strip"></div>
    <ul class="hero-thumbs">
      <li class="thumb-clock" role="img" aria-label="Clock photo"></li>
      <li class="thumb-team" role="img" aria-label="Team photo"></li>
      <li class="thumb-meeting" role="img" aria-label="Meeting photo"></li>
      <li class="thumb-pair" role="img" aria-label="Business colleagues photo"></li>
    </ul>
  </section>

  <main class="features">
    <article class="feature" style="left:0">
      <div class="feature-image img-people" role="img" aria-label="Photo of a business team"></div>
      <h2 class="feature-title">About Vantrel 4<br>Management Limited</h2>
      <p class="feature-text">Lorem ipsum dolor sit amet,<br>consectetuer adipiscing elit.</p>
      <div class="feature-rule"></div>
      <a class="feature-more" href="#">learn more</a>
    </article>
    <article class="feature" style="left:195px">
      <div class="feature-image img-desk" role="img" aria-label="Photo of a manager reviewing documents"></div>
      <h2 class="feature-title">Project Control / Contract<br>Management</h2>
      <p class="feature-text">Lorem ipsum dolor sit amet,<br>consectetuer adipiscing elit.</p>
      <div class="feature-rule"></div>
      <a class="feature-more" href="#">learn more</a>
    </article>
    <article class="feature" style="left:390px">
      <div class="feature-image img-tools" role="img" aria-label="Illustration of a monitor with tools"></div>
      <h2 class="feature-title">Systems, processes<br>and tools</h2>
      <p class="feature-text">Lorem ipsum dolor sit amet,<br>consectetuer adipiscing elit.</p>
      <div class="feature-rule"></div>
      <a class="feature-more" href="#">learn more</a>
    </article>
    <article class="feature" style="left:586px">
      <div class="feature-image img-presenter" role="img" aria-label="Photo of a presentation to colleagues"></div>
      <h2 class="feature-title single">Contract Management</h2>
      <p class="feature-text">Lorem ipsum dolor sit amet,<br>consectetuer adipiscing elit.</p>
      <div class="feature-rule"></div>
      <a class="feature-more" href="#">learn more</a>
    </article>
    <article class="feature" style="left:781px">
      <div class="feature-image img-chart" role="img" aria-label="Photo of a person in front of projected charts"></div>
      <h2 class="feature-title single">Specialist Services</h2>
      <p class="feature-text">Lorem ipsum dolor sit amet,<br>consectetuer adipiscing elit.</p>
      <div class="feature-rule"></div>
      <a class="feature-more" href="#">learn more</a>
    </article>
    <article class="feature" style="left:975px">
      <div class="feature-image img-projects" role="img" aria-label="Collage of reference project images on blue tiles"></div>
      <h2 class="feature-title single">Our reference projects</h2>
      <p class="feature-text">Lorem ipsum dolor sit amet,<br>consectetuer adipiscing elit.</p>
      <div class="feature-rule"></div>
      <a class="feature-more" href="#">learn more</a>
    </article>
  </main>

  <footer class="site-footer">
    <p class="footer-links">Home<span class="sep">|</span>Contact<span class="sep">|</span>Term &amp; Conditions<span class="sep">|</span>Copyright © 2012 Company Name<span class="sep">|</span>All right reserved</p>
  </footer>
</body>
</html>
```